Business Card Design For A Renovation Contractor Company

We need a business card for a new company based in Singapore, our company name is "KT Planora". We are a renovation contractor that builds designs into reality. We build more of F&B restaurants, retail stores and commercial offices. We work very closely with designers. The final design should communicate to our client that we are a company that you can trust, that will plan and complete your project without giving you a headache. I like my client to remember my company as "KT". The beauty of SIMPLE is important.

Industry/Entity Type

Contractor

Requirements
Nice to have
• Black or Red base

```html
<!DOCTYPE html>
<html lang="en">
<head>
<meta charset="utf-8">
<title>KT Planora Business Card</title>
<link rel="stylesheet" href="https://fonts.googleapis.com/css2?family=Arimo:wght@400;700&display=swap">
<style>
  :root {
    --stage: #d9d9d9;
    --stage-light: #ececec;
    --red: #e3222d;
    --red-bright: #f2333d;
    --red-deep: #7a0b12;
    --black: #0d0d0f;
    --charcoal: #1b1b1e;
    --white: #ffffff;
    --text-font: "Arimo", Arial, sans-serif;
  }
  * { box-sizing: border-box; margin: 0; padding: 0; }
  html, body { width: 1200px; height: 861px; overflow: hidden; }
  body {
    background: radial-gradient(ellipse at 50% 40%, var(--stage-light), var(--stage));
    font-family: var(--text-font);
    position: relative;
  }
  .card {
    position: absolute;
    width: 525px;
    height: 300px;
    overflow: hidden;
    border-radius: 3px;
    box-shadow: 0 10px 24px rgba(0,0,0,0.25);
  }
  .card svg.corners { position: absolute; inset: 0; width: 100%; height: 100%; }
  .card--front {
    left: 55px; top: 280px;
    background: linear-gradient(155deg, var(--red-bright) 0%, var(--red) 40%, var(--red-deep) 72%, var(--black) 100%);
  }
  .card--back {
    left: 620px; top: 280px;
    background: linear-gradient(160deg, var(--charcoal), var(--black));
  }
  .brand {
    position: absolute;
    display: flex;
    align-items: center;
    gap: 12px;
  }
  .brand__dot {
    width: 44px; height: 44px;
    border-radius: 50%;
    background: var(--white);
  }
  .brand__name {
    color: var(--white);
    font-weight: 400;
    font-size: 38px;
    letter-spacing: -0.5px;
    line-height: 1;
  }
  .brand__tagline {
    color: var(--white);
    font-size: 14px;
    border-top: 1px solid var(--white);
    margin-top: 4px;
    padding-top: 2px;
    letter-spacing: 0.3px;
  }
  .card--front .brand { left: 110px; top: 118px; }
  .card--back .brand { left: 70px; top: 55px; }
  .person { position: absolute; left: 330px; top: 140px; }
  .person__name { color: var(--red); font-weight: 700; font-size: 25px; }
  .person__role { color: var(--white); font-size: 17px; margin-top: 2px; }
  .contact {
    position: absolute; left: 70px; top: 160px;
    list-style: none;
    color: var(--white);
    font-size: 12px;
    line-height: 1.3;
  }
  .contact li { display: flex; align-items: flex-start; gap: 9px; margin-bottom: 4px; }
  .contact svg { width: 14px; height: 14px; flex: none; margin-top: 1px; }
</style>
</head>
<body>

<section class="card card--front" aria-label="Card front">
  <svg class="corners" viewBox="0 0 525 300" aria-hidden="true">
    <polygon points="440,0 525,0 525,70 500,70 500,30 470,0" fill="#0d0d0f"/>
    <polyline points="470,0 500,30 500,70" fill="none" stroke="#e3222d" stroke-width="3"/>
    <polygon points="0,190 30,190 55,215 55,260 0,260" fill="#0d0d0f"/>
    <polyline points="0,200 25,200 45,220 45,255" fill="none" stroke="#e3222d" stroke-width="3"/>
  </svg>
  <div class="brand">
    <span class="brand__dot"></span>
    <div>
      <div class="brand__name">KT Planora</div>
      <div class="brand__tagline">planned well, built right</div>
    </div>
  </div>
</section>

<section class="card card--back" aria-label="Card back">
  <svg class="corners" viewBox="0 0 525 300" aria-hidden="true">
    <polygon points="420,0 525,0 525,90 505,90 505,35 470,0" fill="#e3222d"/>
    <polygon points="455,0 470,0 505,35 505,90 495,90 495,40" fill="#0d0d0f"/>
    <polygon points="0,150 25,150 50,175 50,300 0,300" fill="#e3222d"/>
    <polygon points="0,165 18,165 38,185 38,300 28,300 28,190 14,176 0,176" fill="#0d0d0f"/>
  </svg>
  <div class="brand">
    <span class="brand__dot"></span>
    <div>
      <div class="brand__name">KT Planora</div>
      <div class="brand__tagline">planned well, built right</div>
    </div>
  </div>
  <div class="person">
    <div class="person__name">Marcus Lim</div>
    <div class="person__role">Director</div>
  </div>
  <ul class="contact">
    <li>
      <svg viewBox="0 0 14 14"><circle cx="7" cy="7" r="7" fill="#e3222d"/><path d="M7 3a2.5 2.5 0 0 0-2.5 2.5C4.5 8 7 11 7 11s2.5-3 2.5-5.5A2.5 2.5 0 0 0 7 3z" fill="#fff"/></svg>
      <span>18 Kallang Way<br>#03-220 Kallang Hub<br>Singapore 349001</span>
    </li>
    <li>
      <svg viewBox="0 0 14 14"><circle cx="7" cy="7" r="7" fill="#e3222d"/><path d="M4.5 3.5l1.5 0 .7 2-1 .8a5 5 0 0 0 2 2l.8-1 2 .7v1.5c-3.5.3-6.3-2.5-6-6z" fill="#fff"/></svg>
      <span>6123 4567</span>
    </li>
    <li>
      <svg viewBox="0 0 14 14"><circle cx="7" cy="7" r="7" fill="#e3222d"/><rect x="5" y="3" width="4" height="8" rx="0.8" fill="#fff"/></svg>
      <span>6123 4567</span>
    </li>
    <li>
      <svg viewBox="0 0 14 14"><circle cx="7" cy="7" r="7" fill="#e3222d"/><rect x="3.5" y="4.5" width="7" height="5" fill="#fff"/><path d="M3.5 4.5L7 7.5l3.5-3" fill="none" stroke="#e3222d" stroke-width="0.8"/></svg>
      <span>marcus@ktplanora.com</span>
    </li>
    <li>
      <svg viewBox="0 0 14 14"><circle cx="7" cy="7" r="7" fill="#e3222d"/><circle cx="7" cy="7" r="3.5" fill="none" stroke="#fff" stroke-width="1"/><path d="M3.5 7h7M7 3.5v7" stroke="#fff" stroke-width="0.8"/></svg>
      <span>www.ktplanora.com</span>
    </li>
  </ul>
</section>

</body>
</html>
```